Its time for a new website

We are at a point now where we are in desperate need of a new website. It was last updated 2006 but still looks like its 1995. We are looking for something eye catching to our clients but easy to navigate and add/remove photos of jobs/trucks and information. Our key business is the manufacture of fire appliances and resale of parts and equipment.

www.dunmorerescue.com.au

Coding

Coded - Design and coding required

Number of Pages Required

5+ page

Requirements
Must have
• Logo

```html
<!DOCTYPE html>
<html lang="en">
<head>
<meta charset="utf-8">
<title>Dunmore Rescue – Fire Appliances</title>
<link rel="stylesheet" href="https://fonts.googleapis.com/css2?family=Exo+2:wght@300;400;500;600&display=swap">
<style>
:root{
  --page:#dfe3e6;
  --grey-mid:#c9cdd0;
  --red:#d8102a;
  --red-soft:#e8412f;
  --red-deep:#d53a2a;
  --blue:#2f80c2;
  --nav-blue:#1a7fc1;
  --navy:#2c3e50;
  --ink:#2f3b48;
  --muted:#7a838c;
  --white:#ffffff;
  --black:#111;
}
*{box-sizing:border-box;margin:0;padding:0}
html,body{width:1200px;height:1000px;overflow:hidden;background:var(--white);font-family:"Exo 2",sans-serif;color:var(--ink)}
.page{position:absolute;left:206px;top:0;width:732px;height:1000px;background:var(--page)}
.abs{position:absolute}
.topbar-phone{left:388px;top:8px;font-size:13px;color:#333}
.social{left:504px;top:10px;display:flex;gap:8px}
.social span{width:12px;height:12px;border-radius:50%;background:#b9bec3;display:block}
.nav{left:51px;top:33px;width:629px;height:42px;background:var(--red)}
.nav ul{list-style:none;position:absolute;right:0;top:0;height:42px;display:flex}
.nav li{height:42px;line-height:42px;padding:0 9px;margin-left:0;color:var(--white);font-size:13px}
.nav li.active{background:var(--nav-blue)}
.brand{left:51px;top:33px;width:107px;height:67px;background:var(--black);display:flex;flex-direction:column;align-items:center;justify-content:center;gap:5px;z-index:2}
.brand i{width:26px;height:26px;border-radius:50%;background:var(--red);display:block}
.brand b{font-weight:600;font-size:11px;color:#3b8fd6}
.hero{left:0;top:75px;width:732px;height:253px}
.hero-left{left:0;top:0;width:394px;height:253px;background:linear-gradient(180deg,#6aa7d8 0%,#c9dbe8 35%,#c3242a 60%,#8e2a2a 100%)}
.hero-right{left:394px;top:0;width:338px;height:253px;background:linear-gradient(180deg,#dfe4e6 0%,#f1f1ee 45%,#b9b9b1 100%)}
.arrow-btn{width:25px;height:26px;background:var(--red);display:flex;align-items:center;justify-content:center}
.caption{color:var(--white);font-size:15.5px;padding:0 6px;height:23px;line-height:23px;white-space:nowrap}
.card{top:328px;width:209px;height:160px;background:var(--white)}
.card.alt{background:#eceeef}
.card .photo{height:79px}
.card h3{font-weight:400;font-size:13px;margin:10px 10px 6px;color:var(--ink)}
.card p{font-size:7px;line-height:10px;margin:0 10px;color:var(--muted)}
.card .more{position:absolute;right:10px;bottom:10px;font-size:7px;color:#333}
.why{left:51px;top:489px;width:210px;height:172px;background:var(--red-soft)}
.why-head{height:51px;background:var(--red-deep);padding:13px 11px;color:var(--white);font-size:12px;line-height:13px;position:relative}
.why-head:after{content:"";position:absolute;left:95px;bottom:-10px;border:10px solid transparent;border-bottom:0;border-top-color:var(--red-deep)}
.why ul{list-style:none;margin:16px 11px}
.why li{color:var(--white);font-size:8.5px;height:16.3px;display:flex;align-items:center;gap:8px}
.ask{left:261px;top:489px;width:210px;height:172px;background:linear-gradient(160deg,#3a8ccc,#2a6fae)}
.ask h3{color:var(--white);font-weight:400;font-size:12.5px;line-height:14px;text-align:center;margin-top:57px}
.ask .btn{display:block;margin:8px auto 0;width:72px;height:18px;background:var(--red-soft);color:var(--white);font-size:6px;text-align:center;line-height:18px}
.products{left:470px;top:489px;width:210px;height:172px;background:var(--navy)}
.products h3{font-weight:400;font-size:12px;color:var(--white);margin:11px 16px}
.link-ico{width:17px;height:17px;background:var(--white);display:flex;align-items:center;justify-content:center}
.products .photo{left:0;top:35px;width:210px;height:96px;background:linear-gradient(180deg,#9dc1dd,#e2e6e6 50%,#a8a497)}
.products .name{top:137px;left:0;width:210px;text-align:center;color:var(--red-soft);font-size:12.5px}
.mini-arrow{width:14px;height:18px;background:rgba(255,255,255,.85);display:flex;align-items:center;justify-content:center}
.block{top:661px;width:210px;height:172px}
.block h3{font-weight:400;font-size:13px;margin:10px 11px;color:var(--ink)}
.quote{left:11px;top:35px;width:189px;height:40px;background:#cfd3d6;font-size:7px;line-height:10px;color:var(--muted);padding:9px 10px}
.quote:after{content:"";position:absolute;left:22px;bottom:-12px;border:12px solid transparent;border-bottom:0;border-top-color:#cfd3d6}
.avatar{left:30px;top:97px;width:38px;height:38px;background:linear-gradient(180deg,#b08d74,#5b4a43)}
.pager{display:flex;gap:1px}
.pager span{width:17px;height:17px;background:var(--white);border:1px solid #d3d6d8;display:flex;align-items:center;justify-content:center}
.post{left:11px;display:flex;gap:9px}
.post .thumb{width:71px;height:48px}
.post h4{font-weight:400;font-size:7px;line-height:9px;color:var(--ink);width:90px;margin-top:2px}
.post small{display:block;font-size:6px;color:var(--muted);margin-top:3px}
.post small em{font-style:normal;color:var(--red-soft)}
.contact-row{left:10px;display:flex;align-items:center;gap:11px;font-size:8.5px;line-height:10px;color:#333}
.contact-row .ico{width:26px;height:26px;background:#cdd1d4;display:flex;align-items:center;justify-content:center;flex:none}
.partners{left:51px;top:834px;width:629px;height:57px;background:var(--grey-mid)}
.partners .badge{top:19px;height:20px;background:#9ba1a6;border-radius:3px}
.footer{left:0;top:902px;width:730px;height:98px;background:var(--navy)}
.footer h3{position:absolute;top:30px;font-weight:400;font-size:13px;color:var(--red-soft)}
.footer p{position:absolute;font-size:7px;line-height:11px;color:var(--white)}
</style>
</head>
<body>
<div class="page">
  <div class="abs topbar-phone">&#9647;+61 5550 1284</div>
  <div class="abs social"><span></span><span></span><span></span><span></span><span></span><span></span><span></span><span></span><span></span></div>

  <nav class="abs nav">
    <ul>
      <li class="active">HOME</li><li>ABOUT</li><li>EQUIPMENT</li><li>NEWS</li><li>CONTACT</li><li style="padding-right:22px;padding-left:13px">BLOG</li>
    </ul>
  </nav>
  <div class="abs brand"><i></i><b>Dunmore Rescue</b></div>

  <section class="abs hero">
    <div class="abs hero-left" role="img" aria-label="Red fire and rescue truck parked under blue sky"></div>
    <div class="abs hero-right" role="img" aria-label="White bushfire appliance truck with bull bar"></div>
    <div class="abs arrow-btn" style="left:13px;top:113px"><svg width="8" height="12"><path d="M6 1 1 6l5 5" stroke="#fff" fill="none" stroke-width="1.4"/></svg></div>
    <div class="abs arrow-btn" style="left:694px;top:113px"><svg width="8" height="12"><path d="M2 1l5 5-5 5" stroke="#fff" fill="none" stroke-width="1.4"/></svg></div>
    <div class="abs caption" style="left:175px;top:172px;background:var(--red)">Western Australia's largest, most experienced and competent</div>
    <div class="abs caption" style="left:204px;top:200px;background:var(--black)">manufacturer of today's fire fighting vehicles</div>
  </section>

  <article class="abs card" style="left:51px">
    <div class="photo" role="img" aria-label="White utility fire unit" style="background:linear-gradient(180deg,#8fb4d6,#d9d4c8 55%,#a88f6b)"></div>
    <h3>SAVE PLENTY OF TIME</h3>
    <p>Ut a nunc. Vivamus est. Suspendisse potenti. In id felis. Vestibulum et magnis dis parturient montes, nascetur ridiculus</p>
    <span class="more">Read more ›</span>
  </article>
  <article class="abs card alt" style="left:261px">
    <div class="photo" role="img" aria-label="Red fire trailer with tank" style="background:linear-gradient(180deg,#a9c3d6,#c64a3a 45%,#c7a98a)"></div>
    <h3>FREE SUPPORT</h3>
    <p>Ut a nunc. Vivamus est. Suspendisse potenti. In id felis. Vestibulum et magnis dis parturient montes, nascetur ridiculus</p>
    <span class="more">Read more ›</span>
  </article>
  <article class="abs card" style="left:470px">
    <div class="photo" role="img" aria-label="Fleet of fire trucks outside the workshop" style="background:linear-gradient(180deg,#7fa6cf,#dcdcd6 50%,#8c8578)"></div>
    <h3>SAVE PLENTY OF TIME</h3>
    <p>Ut a nunc. Vivamus est. Suspendisse potenti. In id felis. Vestibulum et magnis dis parturient montes, nascetur ridiculus</p>
    <span class="more">Read more ›</span>
  </article>

  <section class="abs why">
    <div class="why-head">WHY SHOULD YOU CHOOSE<br>DUNMORE RESCUE?</div>
    <ul>
      <li><svg width="9" height="9"><rect x=".5" y=".5" width="8" height="8" fill="none" stroke="#fff"/><path d="M2 4.5l2 2 4-5" stroke="#fff" fill="none" stroke-width="1.3"/></svg>Sed ipsum primis in augue lorem</li>
      <li><svg width="9" height="9"><rect x=".5" y=".5" width="8" height="8" fill="none" stroke="#fff"/><path d="M2 4.5l2 2 4-5" stroke="#fff" fill="none" stroke-width="1.3"/></svg>Sed ipsum primis in augue lorem</li>
      <li><svg width="9" height="9"><rect x=".5" y=".5" width="8" height="8" fill="none" stroke="#fff"/><path d="M2 4.5l2 2 4-5" stroke="#fff" fill="none" stroke-width="1.3"/></svg>Sed ipsum primis in augue lorem</li>
      <li><svg width="9" height="9"><rect x=".5" y=".5" width="8" height="8" fill="none" stroke="#fff"/><path d="M2 4.5l2 2 4-5" stroke="#fff" fill="none" stroke-width="1.3"/></svg>Sed ipsum primis in augue lorem</li>
      <li><svg width="9" height="9"><rect x=".5" y=".5" width="8" height="8" fill="none" stroke="#fff"/><path d="M2 4.5l2 2 4-5" stroke="#fff" fill="none" stroke-width="1.3"/></svg>Sed ipsum primis in augue lorem</li>
    </ul>
  </section>

  <section class="abs ask" role="img" aria-label="City skyline in blue tint">
    <h3>DO YOU HAVE MORE QUESTIONS<br>ABOUT US?</h3>
    <span class="btn">CONTACT WITH US</span>
  </section>

  <section class="abs products">
    <h3>VIEW ALL OUR PRODUCTS</h3>
    <div class="abs link-ico" style="right:11px;top:9px"><svg width="9" height="9"><path d="M3 6l3-3M2 4.5 1 5.5a1.5 1.5 0 0 0 2.5 2.5l1-1M7 4.5l1-1A1.5 1.5 0 0 0 5.5 1l-1 1" stroke="#555" fill="none"/></svg></div>
    <div class="abs photo" role="img" aria-label="White water tanker truck"></div>
    <div class="abs mini-arrow" style="left:11px;top:71px"><svg width="6" height="10"><path d="M5 1 1 5l4 4" stroke="#555" fill="none"/></svg></div>
    <div class="abs mini-arrow" style="right:11px;top:71px"><svg width="6" height="10"><path d="M1 1l4 4-4 4" stroke="#555" fill="none"/></svg></div>
    <div class="abs name">VESTIBULUM ANTE IPSUM</div>
  </section>

  <section class="abs block" style="left:51px;background:var(--page)">
    <h3>TESTIMONIALS</h3>
    <div class="abs link-ico" style="right:11px;top:9px"><svg width="9" height="9"><path d="M3 6l3-3M2 4.5 1 5.5a1.5 1.5 0 0 0 2.5 2.5l1-1M7 4.5l1-1A1.5 1.5 0 0 0 5.5 1l-1 1" stroke="#555" fill="none"/></svg></div>
    <div class="abs quote">Ha, have to just take off the hat for this<br>Ha, have to just take off the hat for this</div>
    <div class="abs avatar" role="img" aria-label="Client portrait"></div>
    <div class="abs" style="left:75px;top:101px;font-size:8px;color:var(--red-soft)">MARNIE COLE</div>
    <div class="abs pager" style="right:11px;top:145px"><span><svg width="5" height="8"><path d="M4 1 1 4l3 3" stroke="#555" fill="none"/></svg></span><span><svg width="5" height="8"><path d="M1 1l3 3-3 3" stroke="#555" fill="none"/></svg></span></div>
  </section>

  <section class="abs block" style="left:261px;background:var(--white)">
    <h3>BLOG</h3>
    <div class="abs link-ico" style="right:11px;top:9px;background:var(--page)"><svg width="9" height="9"><path d="M3 6l3-3M2 4.5 1 5.5a1.5 1.5 0 0 0 2.5 2.5l1-1M7 4.5l1-1A1.5 1.5 0 0 0 5.5 1l-1 1" stroke="#555" fill="none"/></svg></div>
    <div class="abs post" style="top:33px"><div class="thumb" role="img" aria-label="City street with colourful buildings" style="background:linear-gradient(180deg,#7aa3c7,#b9664a)"></div><div><h4>ETIAM RUTRUM ENIM AC TRISTIQUE</h4><small>27.04.2012 | <em>Comments off</em></small></div></div>
    <div class="abs post" style="top:97px"><div class="thumb" role="img" aria-label="Evening city street" style="background:linear-gradient(180deg,#3a4f7a,#c9874a)"></div><div><h4>SUSPENDISSE A PELLENTESQUE DUI</h4><small>27.04.2012 | <em>Comments off</em></small></div></div>
    <div class="abs pager" style="right:11px;top:145px"><span><svg width="8" height="5"><path d="M1 4l3-3 3 3" stroke="#555" fill="none"/></svg></span><span><svg width="8" height="5"><path d="M1 1l3 3 3-3" stroke="#555" fill="none"/></svg></span></div>
  </section>

  <section class="abs block" style="left:470px;background:var(--page)">
    <h3 style="margin-left:10px">GET IN TOUCH</h3>
    <div class="abs contact-row" style="top:33px"><span class="ico"><svg width="10" height="13"><path d="M5 12S1 7 1 4.5a4 4 0 0 1 8 0C9 7 5 12 5 12z" fill="#fff"/><circle cx="5" cy="4.5" r="1.5" fill="#cdd1d4"/></svg></span>Lot 14 Harlow Road Brenton 6399<br>Western Australia</div>
    <div class="abs contact-row" style="top:67px"><span class="ico"><svg width="12" height="12"><path d="M2 1h3l1 3-2 1a7 7 0 0 0 3 3l1-2 3 1v3c-6 0-10-4-10-10z" fill="#fff"/></svg></span>61 8 5550 2174</div>
    <div class="abs contact-row" style="top:98px"><span class="ico"><svg width="13" height="9"><rect width="13" height="9" fill="#fff"/><path d="M0 0l6.5 5L13 0" stroke="#cdd1d4" fill="none"/></svg></span>info@dunmorerescue.com.au</div>
    <div class="abs contact-row" style="top:129px"><span class="ico"><svg width="12" height="12"><circle cx="6" cy="6" r="5.5" fill="#fff"/><path d="M6 3v3h2" stroke="#cdd1d4" fill="none"/></svg></span>www.dunmorerescue.com.au</div>
  </section>

  <section class="abs partners" aria-label="Partners">
    <div class="abs mini-arrow" style="left:10px;top:20px;background:var(--white)"><svg width="6" height="10"><path d="M5 1 1 5l4 4" stroke="#555" fill="none"/></svg></div>
    <div class="abs badge" style="left:38px;width:78px"></div>
    <div class="abs badge" style="left:135px;width:76px"></div>
    <div class="abs badge" style="left:232px;width:70px"></div>
    <div class="abs badge" style="left:325px;width:74px"></div>
    <div class="abs badge" style="left:420px;width:72px"></div>
    <div class="abs badge" style="left:513px;width:74px"></div>
    <div class="abs mini-arrow" style="right:11px;top:20px;background:var(--white)"><svg width="6" height="10"><path d="M1 1l4 4-4 4" stroke="#555" fill="none"/></svg></div>
  </section>

  <footer class="abs footer">
    <h3 style="left:62px">ABOUT US</h3>
    <p style="left:62px;top:60px;width:190px">Nulla vitae elit libero, a pharetra augue. Curabitur blandit tempus porttitor. Etiam sem malesuada magna mollis euismod. Etiam porta sem malesuada magna mollis.</p>
    <h3 style="left:271px">LATEST POSTS</h3>
    <div class="abs" style="left:271px;top:60px;width:34px;height:22px;background:linear-gradient(180deg,#7aa3c7,#b9664a)" role="img" aria-label="Blog thumbnail"></div>
    <p style="left:313px;top:61px">ETIAM RUTRUM ENIM AC TRISTIQUE<br><span style="font-size:6px;color:#aab3bb">27.04.2012 | Comments off</span></p>
    <div class="abs" style="left:271px;top:92px;width:34px;height:8px;background:linear-gradient(180deg,#3a4f7a,#c9874a)"></div>
    <h3 style="left:480px">RECENT COMMENTS</h3>
    <p style="left:480px;top:60px;width:200px">"There are many variations of passages of Lorem Ipsum available, but the majority have suffered [...]"</p>
    <p style="left:480px;top:84px;font-size:6px">Dale Pryor <span style="color:var(--red-soft)">Vestibulum dapibus mauris</span></p>
  </footer>
</div>
</body>
</html>
```